Online Rug Store needs Clearance Banner

Website is: Lanternfield Carpets and Home
You can access it at: www.lanternfieldcarpetsandhome.com and login (top right) with password: trazok

*** update: When creating banners for my site, you have permission to use images from www.velbora.com, but ONLY for this project. The images/artwork are copyright allowable for use on www.lanternfieldcarpetsandhome.com projects.***

We need a home page banner sized 1000 wide x 500 tall pixels to promote a "Clearance Sale" on rugs. The banner can state:

1. Clearance Sale
2. Now in progress
3. Save an extra 20% with coupon code 'Mint20'
4. Ends March 31st
5. Plus Free Shipping and 30 day returns.

We prefer a banner that appears hand-drawn and artistic, not commercially produced. It is OK to use a room scene image, rug images, or just a colored/textured background with text and no images. Your choice.

Flat graphics with no shadows and 3-D effect preferred.
Attached is are 3 logo options, as well as an example banner with handcrafted, artistic styling that we prefer.

Target Market(s)

This should be an eye-catching banner to showcase a very urgent promotion. Consider using colors of red, white, gold, and black to make a strong statement on the home page.

Industry/Entity Type

Home And Garden

Requirements
Must have
• Winner must provide Photoshop editable file format (.psd format) including layers that can be edited.
Nice to have
• Hand-drawn, stenciled, scribbled, artistic graphics and fonts is nice because we sell rugs that are made by hand.
Should not have
• little to no shadowing. Avoid computerized graphics.

```html
<!DOCTYPE html>
<html lang="en">
<head>
<meta charset="utf-8">
<title>Clearance Sale Banner – Lanternfield Carpets and Home</title>
<link rel="stylesheet" href="https://fonts.googleapis.com/css2?family=Pacifico&family=Courgette&family=Questrial&family=Open+Sans:wght@700&family=Cinzel:wght@400&display=swap">
<style>
  :root {
    --page-bg: #e4e4e4;
    --maroon: #4a0709;
    --gold: #c8a43a;
    --gold-deep: #b8962a;
    --sign-fill: #5b3333;
    --sign-edge: #8c6c6c;
    --white: #ffffff;
    --ink-dark: #4a0709;
    --black: #000000;
  }
  html, body {
    margin: 0;
    width: 1200px;
    height: 800px;
    overflow: hidden;
    background: var(--page-bg);
  }
  .banner {
    position: absolute;
    left: 100px;
    top: 150px;
    width: 1000px;
    height: 500px;
    overflow: hidden;
  }
  .banner-texture {
    position: absolute;
    inset: 0;
    background: var(--maroon);
  }
  .headline {
    position: absolute;
    left: 64px;
    top: 40px;
    margin: 0;
    font-family: "Pacifico", cursive;
    font-weight: 400;
    font-size: 70px;
    line-height: 1.3;
    color: var(--gold);
    white-space: nowrap;
  }
  .status {
    position: absolute;
    left: 200px;
    top: 163px;
    font-family: "Questrial", sans-serif;
    font-size: 30px;
    color: var(--white);
    white-space: nowrap;
  }
  .hanger {
    position: absolute;
    left: 260px;
    top: 210px;
  }
  .deadline-sign {
    position: absolute;
    left: 180px;
    top: 308px;
    width: 276px;
    height: 88px;
    box-sizing: border-box;
    background: var(--sign-fill);
    border: 3px solid var(--sign-edge);
    border-radius: 4px;
    display: flex;
    align-items: center;
    justify-content: center;
    font-family: "Courgette", cursive;
    font-style: italic;
    font-size: 27px;
    color: var(--gold);
  }
  .perks {
    position: absolute;
    left: 178px;
    top: 420px;
    font-family: "Questrial", sans-serif;
    font-size: 14.5px;
    letter-spacing: 0.3px;
    color: var(--white);
    white-space: nowrap;
  }
  .coupon-bubble {
    position: absolute;
    left: 600px;
    top: 58px;
  }
  .coupon-text {
    position: absolute;
    left: 612px;
    top: 112px;
    width: 170px;
    text-align: center;
    font-family: "Open Sans", sans-serif;
    font-weight: 700;
    font-size: 16.5px;
    line-height: 1.2;
    color: var(--ink-dark);
  }
  .brand-panel {
    position: absolute;
    left: 535px;
    top: 310px;
    width: 465px;
    height: 140px;
    background: var(--black);
    display: flex;
    align-items: center;
    gap: 18px;
    padding-left: 60px;
    box-sizing: border-box;
  }
  .brand-mark {
    width: 54px;
    height: 54px;
    background: var(--white);
    flex: none;
  }
  .brand-name {
    font-family: "Cinzel", serif;
    font-weight: 400;
    font-size: 25px;
    line-height: 1.15;
    color: var(--white);
    letter-spacing: 1px;
  }
</style>
</head>
<body>
  <main class="banner">
    <div class="banner-texture" role="img" aria-label="Deep maroon background with a subtle zigzag pattern"></div>

    <h1 class="headline">Clearance Sale!</h1>
    <p class="status" style="margin:0">Now in progress</p>

    <svg class="hanger" width="120" height="110" viewBox="0 0 120 110" aria-hidden="true">
      <g stroke="#ffffff" stroke-width="2.5" stroke-dasharray="2 3" fill="none" stroke-linecap="round">
        <line x1="62" y1="2" x2="12" y2="102"/>
        <line x1="62" y1="2" x2="110" y2="102"/>
      </g>
      <circle cx="12" cy="102" r="4" fill="#555"/>
      <circle cx="110" cy="102" r="4" fill="#555"/>
    </svg>

    <div class="deadline-sign">Ends March 31st</div>
    <p class="perks" style="margin:0">Free Shipping and 30 day returns.</p>

    <svg class="coupon-bubble" width="200" height="230" viewBox="0 0 200 230" aria-hidden="true">
      <path d="M175 180 L215 222 L185 150 Z" fill="var(--gold-deep)" transform="translate(-30 0)"/>
      <circle cx="97" cy="97" r="96" fill="var(--gold-deep)"/>
      <circle cx="97" cy="97" r="86" fill="none" stroke="#ffffff" stroke-width="2.5" stroke-dasharray="5 4"/>
    </svg>
    <p class="coupon-text" style="margin:0">Save an<br>extra 20% with<br>coupon code<br>'Mint20'</p>

    <div class="brand-panel">
      <div class="brand-mark"></div>
      <div class="brand-name">Lanternfield<br>Carpets and Home</div>
    </div>
  </main>
</body>
</html>
```